M Zyvantics Buisness Cards

I need a technology focused clean business card for my employees. I have attached out logo to include in the mocks. We're a modern tech consulting firm that drives to interface humanity with technology in a truly cohesive fashion.

```html
<!DOCTYPE html>
<html lang="en">
<head>
<meta charset="utf-8">
<title>M Zyvantics Business Cards</title>
<link href="https://fonts.googleapis.com/css2?family=Lato:wght@400;700&display=swap" rel="stylesheet">
<style>
  :root {
    --page: #2b2d31;
    --card: #1f1f21;
    --blue: #1f74cc;
    --grey: #8c8c8f;
    --text: #f2f2f2;
    --rule: #6e6e72;
  }
  * { box-sizing: border-box; margin: 0; padding: 0; }
  html, body { width: 1200px; height: 900px; overflow: hidden; }
  body {
    background: var(--page);
    font-family: "Lato", sans-serif;
    display: flex;
    flex-direction: column;
    align-items: center;
    justify-content: center;
    gap: 60px;
  }
  .card {
    position: relative;
    width: 525px;
    height: 300px;
    background: var(--card);
    border-radius: 22px;
    overflow: hidden;
    box-shadow: 0 18px 40px rgba(0,0,0,0.45);
  }
  .brand {
    display: flex;
    align-items: center;
    gap: 10px;
    font-weight: 700;
    color: var(--grey);
    white-space: nowrap;
  }
  .brand-dot {
    border-radius: 50%;
    background: var(--blue);
    flex: none;
  }
  /* back */
  .card-back { display: flex; flex-direction: column; align-items: center; justify-content: center; gap: 26px; }
  .card-back .brand { font-size: 40px; }
  .card-back .brand-dot { width: 26px; height: 26px; }
  .card-back .site { color: var(--text); font-size: 14px; letter-spacing: 3px; }
  /* front */
  .card-front { display: flex; align-items: center; padding: 0 0 14px 30px; }
  .card-front .brand { font-size: 24px; width: 176px; align-self: flex-start; margin-top: 78px; }
  .card-front .brand-dot { width: 16px; height: 16px; }
  .divider { width: 1px; height: 200px; background: var(--rule); margin: 0 22px 0 10px; flex: none; }
  .details { display: flex; flex-direction: column; width: 262px; }
  .title-block { display: flex; flex-direction: column; align-items: flex-end; align-self: flex-start; margin-bottom: 14px; }
  .name { color: var(--blue); font-size: 27px; font-weight: 400; line-height: 1.1; white-space: nowrap; }
  .role { color: var(--grey); font-size: 16px; line-height: 1.2; }
  .contact { list-style: none; display: flex; flex-direction: column; gap: 7px; }
  .contact li { display: flex; align-items: center; gap: 8px; color: var(--text); font-size: 13px; white-space: nowrap; }
  .contact svg { width: 13px; height: 13px; flex: none; fill: var(--grey); }
  .band { position: absolute; left: 0; right: 0; bottom: 0; height: 14px; background: var(--blue); }
</style>
</head>
<body>
  <section class="card card-back">
    <div class="brand"><span class="brand-dot"></span>M Zyvantics</div>
    <p class="site">www.zyvanticsgroup.com</p>
  </section>

  <section class="card card-front">
    <div class="brand"><span class="brand-dot"></span>M Zyvantics</div>
    <div class="divider"></div>
    <div class="details">
      <div class="title-block">
        <h1 class="name">Person's Name</h1>
        <p class="role">Funder</p>
      </div>
      <ul class="contact">
        <li><svg viewBox="0 0 24 24"><path d="M6.6 10.8a15.1 15.1 0 0 0 6.6 6.6l2.2-2.2a1 1 0 0 1 1-.25 11.4 11.4 0 0 0 3.6.57 1 1 0 0 1 1 1V20a1 1 0 0 1-1 1A17 17 0 0 1 3 4a1 1 0 0 1 1-1h3.5a1 1 0 0 1 1 1c0 1.25.2 2.45.57 3.57a1 1 0 0 1-.25 1z"/></svg>(555)014-2870</li>
        <li><svg viewBox="0 0 24 24"><path d="M2 5h20v14H2z M3.5 6.5 12 13l8.5-6.5" fill="none" stroke="#8c8c8f" stroke-width="2"/></svg>nora@zyvanticsgroup.com</li>
        <li><svg viewBox="0 0 24 24"><circle cx="12" cy="12" r="9" fill="none" stroke="#8c8c8f" stroke-width="2"/><path d="M3 12h18M12 3c3 3 3 15 0 18M12 3c-3 3-3 15 0 18" fill="none" stroke="#8c8c8f" stroke-width="1.6"/></svg>www.zyvanticsgroup.com</li>
        <li><svg viewBox="0 0 24 24"><path d="M12 3 2 12h3v9h5v-6h4v6h5v-9h3z"/></svg>P.O Box 480213 Harlow, Texas 75099</li>
      </ul>
    </div>
    <div class="band"></div>
  </section>
</body>
</html>
```